Invitation annual meeting 2017 of Corvelle Group (2017 Annual Staff Appointments)

Version française: We want to create an invitation to the annual meeting of Groupe Corvelle. This invitation will also be printed as a poster. You will find enclosed a photo of a "B" made with the employees of the Group during an internal event. You will absolutely have this photo on the invitation. I also send it to you when you save it while waiting for the invitation. The invitation must be festive, elegant and classy, ​​because it will take place on the 18th of December, just before Christmas (on the theme of Christmas and New Year Eve). Please, do not use the color "red" on this invitation. You can use this gray: Pantone 431 C for this invitation if you want to. The annual meeting of the staff (annual meeting) 18 December 2017 (18th) of December 2017) Marlindôme (at Marlindome) From 5pm to 9.30pm (from 5pm to 9.30pm) French version: On the occasion of the annual meeting of the staff we wish to make an invitation which will also be printed as a poster. You will find in the attached elements a photo of a B made on the beach with employees. It will be necessary to use this B imperatively for your creation. I am also sending you the quick save the date we had done while waiting for the invitation. This one must be classy, ​​festive because the event will take place on December 18th, with the approach of the end-of-year celebrations (thematic New Year's Eve and non-christmas). You can use anthracite gray: Pantone 431C The group logo should appear on the invitation. Text: Annual Staff Meeting 18 December 2017 Marlindôme from 5pm to 9.30pm
Updates

Project Deadline Extended Reason: Hello We give two more days on the project because we have not been fully seduced by the proposals received so far. Added Tuesday, October 24, 2017

Target Market(s)

ENG: Internal ==> employees of the Corvelle Group FR: internal to the Group

Colors

Requirements
Must have
• ENG: It is obligatory to use the photo of the "B" on the beach for this invitation. You can crop the image of the B if you want to. FR: B "made by employees" of the transmitted photo (possibility of detaching it)
Should not have
• ENG: Boat photos, "kitsch" designs and the color red EN: the pictures of boats, the "kitsch", the red

```html
<!DOCTYPE html>
<html lang="fr">
<head>
<meta charset="utf-8">
<title>Rendez-vous Annuel du Personnel — Groupe Corvelle</title>
<link href="https://fonts.googleapis.com/css2?family=Pinyon+Script&family=Libre+Baskerville:ital@0;1&display=swap" rel="stylesheet">
<style>
  :root {
    --page: #ffffff;
    --sand-light: #cdc9c4;
    --sand: #c0bcb7;
    --sand-dark: #aeaaa5;
    --ink: #ffffff;
    --crowd-a: #5a5f8c;
    --crowd-b: #7a86b0;
    --crowd-c: #8fa6b8;
  }
  * { margin: 0; padding: 0; box-sizing: border-box; }
  html, body {
    width: 1200px; height: 778px; overflow: hidden;
    background: var(--page);
  }
  .invitation {
    position: absolute; left: 107px; top: 70px;
    width: 989px; height: 641px;
    background: radial-gradient(ellipse at 40% 45%, var(--sand-light) 0%, var(--sand) 60%, var(--sand-dark) 100%);
  }
  .invitation__frame {
    position: absolute; left: 29px; top: 30px;
    width: 931px; height: 582px;
    border: 1.5px solid var(--ink);
  }
  .invitation__crowd {
    position: absolute; left: 532px; top: 115px;
    width: 425px; height: 437px;
  }
  .title {
    position: absolute; color: var(--ink);
    font-family: "Pinyon Script", cursive;
    font-weight: 400; line-height: 1; white-space: nowrap;
  }
  .title--rendezvous { left: 76px; top: 100px; font-size: 84px; }
  .title--annuel { left: 250px; top: 178px; font-size: 82px; }
  .title--personnel { left: 86px; top: 288px; font-size: 70px; }
  .title--personnel .title__small { font-size: 40px; margin-right: 12px; }
  .details {
    position: absolute; left: 183px; top: 424px; width: 220px;
    text-align: center; color: var(--ink);
    font-family: "Libre Baskerville", serif; font-style: italic;
    font-size: 16px; line-height: 21px;
  }
  .brand {
    position: absolute; left: 103px; top: 554px;
    display: flex; align-items: center; gap: 12px;
    color: var(--ink);
    font-family: "Libre Baskerville", serif; font-weight: 400;
    font-size: 21px; letter-spacing: 6px; white-space: nowrap;
  }
  .brand__mark { width: 12px; height: 12px; background: var(--ink); }
</style>
</head>
<body>
  <main class="invitation">
    <div class="invitation__frame"></div>

    <svg class="invitation__crowd" viewBox="0 0 425 437" role="img" aria-label="Photographie aérienne des collaborateurs du groupe formant une grande lettre sur la plage">
      <defs>
        <linearGradient id="crowdTones" x1="0" y1="0" x2="1" y2="1">
          <stop offset="0" stop-color="var(--crowd-a)"/>
          <stop offset="0.5" stop-color="var(--crowd-b)"/>
          <stop offset="1" stop-color="var(--crowd-c)"/>
        </linearGradient>
      </defs>
      <rect x="0" y="0" width="425" height="437" rx="50" fill="url(#crowdTones)" opacity="0.8"/>
    </svg>

    <h1>
      <span class="title title--rendezvous">Rendez-vous</span>
      <span class="title title--annuel">Annuel</span>
      <span class="title title--personnel"><span class="title__small">du</span>Personnel</span>
    </h1>

    <p class="details">18 Décembre 2017<br>Au Marlindôme<br>de 17H à 21H30</p>

    <div class="brand"><span class="brand__mark"></span>GROUPE CORVELLE</div>
  </main>
</body>
</html>
```